3 Simple Banners for Travel Company

We need 3 banners created:

728x90
468x60

160x600
120x600

300x250
250x250

There maybe 6 banners above but all we need is 3 designs and then to make that design fit the other banner. E.g. 728 banner is shrank to fit into a 468, BUT use the same design. This is required for 3 banner designs.

These must NOT be flash, only .gif and very professional looking.

please review our website to see and know the look and feel we are looking for: www.crewvoyago.eu
Updates

sorry guys the banner is meant to be 300x250 NOT 250x300

Thanks

Hi there,

We also have another project open if any of you are interested

http://jobs.pixelbidhub.com/job.aspx?id=58219

Thanks

Target Market(s)

travel industry employees (pilots, cabin crew, cruise ship staff, hotel staff etc...)

Industry/Entity Type

It Company

Requirements
Must have
• company logo

company mascots (tim & rosalind)

qz and chirpnet logo

Must inc the following words:

Interline Rates & Travel Discounts
Travel Industry Employees
Sign Up for FREE

```html
<!DOCTYPE html>
<html lang="en">
<head>
<meta charset="utf-8">
<title>CrewVoyago.eu banner set</title>
<link rel="stylesheet" href="https://fonts.googleapis.com/css2?family=Oswald:wght@300;400&display=swap">
<style>
  :root {
    --page: #ffffff;
    --night: #25243a;
    --skyline: #15141d;
    --plane: #1b1a28;
    --logo: #dcd6c8;
    --card: #ffffff;
    --ink: #1f1e2c;
    --red: #c11f2e;
    --blue: #1f9be0;
    --pilot: #2c2b33;
    --crew: #d8402a;
  }
  * { margin: 0; padding: 0; box-sizing: border-box; }
  html, body { width: 1200px; height: 732px; overflow: hidden; background: var(--page); }
  body { position: relative; font-family: "Oswald", sans-serif; }

  .banner { position: absolute; overflow: hidden; background: var(--night); }
  .banner > * { position: absolute; }

  .logo { color: var(--logo); font-weight: 400; line-height: 1; white-space: nowrap; letter-spacing: 0.5px; }

  .plane { background: var(--plane); border-radius: 40% 60% 30% 50%; opacity: 0.9; }
  .skyline { left: 0; right: 0; bottom: 0; background: linear-gradient(to bottom, #1d1c28, var(--skyline)); }

  .mascot { border-radius: 40% 40% 6px 6px; }
  .mascot--pilot { background: linear-gradient(to bottom, #3a3942, var(--pilot)); }
  .mascot--crew { background: linear-gradient(to bottom, #e0553a, var(--crew)); }

  .message { background: var(--card); border-radius: 6px; display: flex; flex-direction: column; justify-content: center; text-align: center; line-height: 1.02; }
  .message .dark { color: var(--ink); }
  .message .red { color: var(--red); }

  .signup { width: 132px; height: 30px; background: var(--card); border-radius: 3px; display: flex; align-items: center; gap: 8px; padding: 0 6px; box-shadow: 0 1px 2px rgba(0,0,0,0.4); }
  .signup__icon { width: 26px; height: 20px; background: var(--blue); border-radius: 2px; display: flex; align-items: center; justify-content: center; }
  .signup__label { font-size: 14px; font-weight: 300; color: var(--ink); white-space: nowrap; }
</style>
</head>
<body>

<!-- Skyscraper: pilot -->
<section class="banner" style="left:31px;top:57px;width:160px;height:600px;">
  <div class="plane" role="img" aria-label="Airliner silhouette" style="left:50px;top:95px;width:110px;height:55px;"></div>
  <p class="logo" style="left:12px;top:18px;font-size:34px;">Crew</p>
  <p class="logo" style="left:12px;top:58px;font-size:32px;">Voyago.eu</p>
  <div class="mascot mascot--pilot" role="img" aria-label="Pilot mascot Tim in captain's uniform" style="left:20px;top:120px;width:125px;height:170px;"></div>
  <div class="skyline" role="img" aria-label="City skyline silhouette" style="height:120px;"></div>
  <div class="message" style="left:8px;top:287px;width:144px;height:193px;">
    <span class="dark" style="font-size:36px;">INTERLINE</span>
    <span class="dark" style="font-size:38px;">RATES &amp;</span>
    <span class="red" style="font-size:42px;">TRAVEL</span>
    <span class="red" style="font-size:29px;">DISCOUNTS</span>
  </div>
  <div class="signup" style="left:15px;top:522px;">
    <span class="signup__icon"><svg width="16" height="12" viewBox="0 0 16 12"><path d="M1 4.5h8V1l6 5-6 5V7.5H1z" fill="#fff"/></svg></span>
    <span class="signup__label">SignUp for FREE</span>
  </div>
</section>

<!-- Skyscraper: cabin crew -->
<section class="banner" style="left:217px;top:57px;width:160px;height:600px;">
  <div class="plane" role="img" aria-label="Airliner silhouette" style="left:50px;top:95px;width:110px;height:55px;"></div>
  <p class="logo" style="left:12px;top:18px;font-size:34px;">Crew</p>
  <p class="logo" style="left:12px;top:58px;font-size:32px;">Voyago.eu</p>
  <div class="mascot mascot--crew" role="img" aria-label="Flight attendant mascot Rosalind in red uniform" style="left:45px;top:125px;width:100px;height:165px;"></div>
  <div class="skyline" role="img" aria-label="City skyline silhouette" style="height:120px;"></div>
  <div class="message" style="left:8px;top:287px;width:144px;height:193px;">
    <span class="dark" style="font-size:46px;">TRAVEL</span>
    <span class="dark" style="font-size:36px;">INDUSTRY</span>
    <span class="red" style="font-size:29px;">EMPLOYEES</span>
  </div>
  <div class="signup" style="left:15px;top:522px;">
    <span class="signup__icon"><svg width="16" height="12" viewBox="0 0 16 12"><path d="M1 4.5h8V1l6 5-6 5V7.5H1z" fill="#fff"/></svg></span>
    <span class="signup__label">SignUp for FREE</span>
  </div>
</section>

<!-- Medium rectangle: pilot -->
<section class="banner" style="left:392px;top:181px;width:300px;height:250px;">
  <div class="plane" role="img" aria-label="Airliner silhouette" style="left:170px;top:5px;width:120px;height:60px;"></div>
  <div class="skyline" role="img" aria-label="City skyline silhouette" style="height:60px;"></div>
  <p class="logo" style="left:18px;top:20px;font-size:40px;">CrewVoyago.eu</p>
  <div class="mascot mascot--pilot" role="img" aria-label="Pilot mascot Tim in captain's uniform" style="left:192px;top:78px;width:108px;height:172px;"></div>
  <div class="message" style="left:10px;top:93px;width:190px;height:80px;">
    <span class="dark" style="font-size:24px;">INTERLINE RATES &amp;</span>
    <span class="red" style="font-size:24px;">TRAVEL DISCOUNTS</span>
  </div>
  <div class="signup" style="left:40px;top:195px;">
    <span class="signup__icon"><svg width="16" height="12" viewBox="0 0 16 12"><path d="M1 4.5h8V1l6 5-6 5V7.5H1z" fill="#fff"/></svg></span>
    <span class="signup__label">SignUp for FREE</span>
  </div>
</section>

<!-- Medium rectangle: cabin crew -->
<section class="banner" style="left:708px;top:181px;width:300px;height:250px;">
  <div class="plane" role="img" aria-label="Airliner silhouette" style="left:170px;top:5px;width:120px;height:60px;"></div>
  <div class="skyline" role="img" aria-label="City skyline silhouette" style="height:60px;"></div>
  <p class="logo" style="left:18px;top:20px;font-size:40px;">CrewVoyago.eu</p>
  <div class="mascot mascot--crew" role="img" aria-label="Flight attendant mascot Rosalind in red uniform" style="left:198px;top:78px;width:90px;height:172px;"></div>
  <div class="message" style="left:10px;top:93px;width:185px;height:80px;">
    <span class="dark" style="font-size:26px;">TRAVEL INDUSTRY</span>
    <span class="red" style="font-size:38px;">EMPLOYEES</span>
  </div>
  <div class="signup" style="left:40px;top:195px;">
    <span class="signup__icon"><svg width="16" height="12" viewBox="0 0 16 12"><path d="M1 4.5h8V1l6 5-6 5V7.5H1z" fill="#fff"/></svg></span>
    <span class="signup__label">SignUp for FREE</span>
  </div>
</section>

<!-- Leaderboard: pilot -->
<section class="banner" style="left:392px;top:448px;width:728px;height:90px;">
  <div class="skyline" role="img" aria-label="City skyline silhouette" style="height:40px;"></div>
  <p class="logo" style="left:18px;top:22px;font-size:40px;">CrewVoyago.eu</p>
  <div class="message" style="left:296px;top:8px;width:226px;height:74px;">
    <span class="dark" style="font-size:25px;">INTERLINE RATES &amp;</span>
    <span class="red" style="font-size:25px;">TRAVEL DISCOUNTS</span>
  </div>
  <div class="mascot mascot--pilot" role="img" aria-label="Pilot mascot Tim in captain's uniform" style="left:514px;top:2px;width:80px;height:88px;"></div>
  <div class="signup" style="left:586px;top:25px;">
    <span class="signup__icon"><svg width="16" height="12" viewBox="0 0 16 12"><path d="M1 4.5h8V1l6 5-6 5V7.5H1z" fill="#fff"/></svg></span>
    <span class="signup__label">SignUp for FREE</span>
  </div>
</section>

<!-- Leaderboard: cabin crew -->
<section class="banner" style="left:392px;top:549px;width:728px;height:90px;">
  <div class="skyline" role="img" aria-label="City skyline silhouette" style="height:40px;"></div>
  <p class="logo" style="left:18px;top:22px;font-size:40px;">CrewVoyago.eu</p>
  <div class="message" style="left:296px;top:8px;width:226px;height:74px;">
    <span class="dark" style="font-size:25px;">TRAVEL INDUSTRY</span>
    <span class="red" style="font-size:36px;">EMPLOYEES</span>
  </div>
  <div class="mascot mascot--crew" role="img" aria-label="Flight attendant mascot Rosalind in red uniform" style="left:516px;top:0;width:66px;height:90px;"></div>
  <div class="signup" style="left:586px;top:25px;">
    <span class="signup__icon"><svg width="16" height="12" viewBox="0 0 16 12"><path d="M1 4.5h8V1l6 5-6 5V7.5H1z" fill="#fff"/></svg></span>
    <span class="signup__label">SignUp for FREE</span>
  </div>
</section>

</body>
</html>
```